Solar Company Bussiness Card

I need a 2 sided business card and would like a .psd and any font files for each side of the card. I would like my logo used, it should be attached with the fonts. I'm not opposed to the font colors with the logo being changed.

On the sample design, I'd like the following:

Darren Pellow
President
Phone: 555-318-2947
www.sunvaleenergyco.example

As I've recently opened in a 2nd market, I'm not sure about an address as I currently have 2 of them. I may actually get separate cards printed, one batch for each address, that's why I need the PSD file.
Updates

I'm very pleased with the response and designs I've received here for my business card. First and foremost, I'd like to thank everyone who took the time to submit a design. There truly are a lot of great designs in the bunch here and I'm having a little difficulty deciding. I will be reaching out to someone in the next day or two here to go to a final design. At this time, I'm not looking for any new concepts. If any of you do logos, I'm looking for a new logo for our sister entity, Pellow Partners, Inc. Thanks, Darren Pellow

Reason: I'm not looking for any new designs at this point, but extending this deadline in order to give people I've asked a chance to re-submit items.

Industry/Entity Type

Business

```html
<!DOCTYPE html>
<html lang="en">
<head>
<meta charset="utf-8">
<title>Sunvale Energy — Business Card</title>
<link rel="stylesheet" href="https://fonts.googleapis.com/css2?family=Open+Sans:wght@400;600&display=swap">
<style>
  :root {
    --backdrop: #e6e7e9;
    --card: #ffffff;
    --card-shade: #f1f2f4;
    --navy: #1d5590;
    --sky: #3b8fd4;
    --ink: #2e2e2e;
    --muted: #6a6a6a;
  }
  * { margin: 0; padding: 0; box-sizing: border-box; }
  html, body {
    width: 1200px; height: 871px; overflow: hidden;
    background: var(--backdrop);
    font-family: "Open Sans", sans-serif;
  }
  .stage { position: relative; width: 1200px; height: 871px; }
  .card {
    position: absolute;
    width: 520px; height: 297px;
    background: linear-gradient(160deg, var(--card) 55%, var(--card-shade));
    box-shadow: 0 6px 18px rgba(0,0,0,0.18);
    overflow: hidden;
  }
  .card--back { left: 60px; top: 287px; }
  .card--front { left: 620px; top: 287px; }

  .brand { display: flex; align-items: center; gap: 10px; }
  .brand__mark { width: 26px; height: 26px; background: var(--sky); }
  .brand__name {
    font-weight: 600; color: var(--navy); letter-spacing: 0.5px;
    line-height: 1;
  }
  .card--back .brand { position: absolute; left: 130px; top: 128px; }
  .card--back .brand__name { font-size: 36px; }

  .card--front .brand { position: absolute; left: 70px; top: 38px; }
  .card--front .brand__mark { width: 30px; height: 30px; }
  .card--front .brand__name { font-size: 38px; }

  .person { position: absolute; left: 70px; top: 130px; }
  .person__name { font-size: 17px; color: var(--ink); letter-spacing: 0.6px; }
  .person__role { font-size: 12px; color: var(--sky); letter-spacing: 0.4px; }

  .contact { position: absolute; left: 58px; top: 190px; list-style: none; }
  .contact__item {
    display: flex; align-items: center; gap: 12px;
    font-size: 12.5px; color: var(--ink); letter-spacing: 1px;
    margin-bottom: 10px;
  }
  .contact__icon { width: 16px; height: 16px; flex: none; }

  .solar-corner { position: absolute; right: 0; bottom: 0; width: 240px; height: 120px; }
</style>
</head>
<body>
<main class="stage">
  <section class="card card--back" aria-label="Card back">
    <div class="brand">
      <span class="brand__mark"></span>
      <span class="brand__name">Sunvale Energy</span>
    </div>
  </section>

  <section class="card card--front" aria-label="Card front">
    <div class="brand">
      <span class="brand__mark"></span>
      <span class="brand__name">Sunvale Energy</span>
    </div>

    <div class="person">
      <p class="person__name">Darren Pellow</p>
      <p class="person__role">President</p>
    </div>

    <ul class="contact">
      <li class="contact__item">
        <svg class="contact__icon" viewBox="0 0 16 16" aria-hidden="true">
          <path d="M2 6 C2 3 14 3 14 6 L11 7 L10 5 H6 L5 7 Z" fill="var(--navy)"/>
          <rect x="4" y="8" width="8" height="6" rx="1.5" fill="none" stroke="var(--navy)" stroke-width="1.4"/>
          <circle cx="8" cy="11" r="1.3" fill="var(--navy)"/>
        </svg>
        <span>555-318-2947</span>
      </li>
      <li class="contact__item">
        <svg class="contact__icon" viewBox="0 0 16 16" aria-hidden="true">
          <circle cx="8" cy="8" r="6.5" fill="none" stroke="var(--navy)" stroke-width="1.4"/>
          <ellipse cx="8" cy="8" rx="2.8" ry="6.5" fill="none" stroke="var(--navy)" stroke-width="1.1"/>
          <line x1="1.5" y1="8" x2="14.5" y2="8" stroke="var(--navy)" stroke-width="1.1"/>
        </svg>
        <span>www.sunvaleenergyco.example</span>
      </li>
    </ul>

    <svg class="solar-corner" viewBox="0 0 240 120" role="img" aria-label="Decorative solar panel cells sweeping across the corner">
      <defs>
        <linearGradient id="cornerFill" x1="0" y1="0" x2="1" y2="1">
          <stop offset="0" stop-color="#4d9de0"/>
          <stop offset="1" stop-color="#1d5590"/>
        </linearGradient>
      </defs>
      <path d="M0 120 C60 70 150 20 240 0 L240 120 Z" fill="url(#cornerFill)"/>
    </svg>
  </section>
</main>
</body>
</html>
```